Veltrane Professional Services Website

Small website for company presence and information. Company is an IT/Telecom services company. We provide presales and installation services. Included are various company logos including color levels. Site doesn't have to use these exact colors in the logos, but should be complimentary if using different colors. It should have a professional business appearance.
Updates

My apologies for not being more responsive on the designs that have been submitted. I will be narrowing down the submissions and providing additional feedback next week. Thank you for your patience.

Project Deadline Extended
Reason: Sorry again for delays on picking designs. Work has me very busy and I've just not had the time to devote to this project. I am extending the design deadline for a few more days to give me time to make my final decisions. Thank you all for your patience. Stay tuned....

Target Market(s)

Telecom sales companies that sell Brintel telecom products.

Industry/Entity Type

Professional Service

Coding

Coded - Design and coding required

Number of Pages Required

5+ page

Font styles to use
Sans Serif

Colors
3276b5
0355a3
85abd2
85cae6
33a6d7
0692cd
ffffff

Requirements
Must have
• Professional design reflective of IT/Telecom business. A good reference website would be: http://www.quollanetworks.example/. Looking for something similar in function and presence.
Nice to have
• Rolling photos highlighting our services. Traditional navigation across the top of all pages.
Should not have
• No motion video, flashy presentation or overly confused interface.

```html
<!DOCTYPE html>
<html lang="en">
<head>
<meta charset="utf-8">
<title>Veltrane Professional Services</title>
<link rel="stylesheet" href="https://fonts.googleapis.com/css2?family=Roboto+Slab:wght@400;700&family=Raleway:wght@400;500;600;700&family=Open+Sans:ital,wght@0,400;0,600;1,400&display=swap">
<style>
:root{
  --navy:#142f5c;
  --blue:#1e6fb8;
  --blue-mid:#0355a3;
  --blue-light:#3276b5;
  --ink:#222;
  --text:#444;
  --grey-bg:#efefef;
  --line:#c9c9c9;
  --white:#fff;
}
*{box-sizing:border-box;margin:0;padding:0}
html,body{width:1200px;height:2643px;overflow:hidden}
body{font-family:"Open Sans",Arial,sans-serif;color:var(--text);background:var(--white);position:relative}

/* header */
.site-header{position:relative;height:100px;background:var(--white)}
.brand{position:absolute;left:162px;top:28px;display:flex;align-items:center;gap:12px}
.brand-square{width:40px;height:40px;background:var(--blue-mid)}
.brand-name{font-family:"Raleway",sans-serif;font-weight:700;color:var(--blue-mid);line-height:1}
.brand-name .big{display:block;font-size:36px;letter-spacing:1px}
.brand-name .small{display:block;font-size:14px;letter-spacing:2px;margin-top:3px}
.top-strip{position:absolute;right:0;top:0;width:504px;height:32px;background:#e4e6e8;border-bottom-left-radius:28px;display:flex;align-items:center;padding-left:20px;gap:10px}
.top-phone{display:flex;align-items:center;gap:6px;font:600 14px "Open Sans",sans-serif;color:var(--navy);margin-right:14px}
.phone-dot{width:24px;height:24px;border-radius:50%;background:var(--navy);display:flex;align-items:center;justify-content:center}
.social-ring{width:30px;height:24px;border:1.5px solid var(--blue-light);border-radius:50%}
.schedule-btn{position:absolute;left:823px;top:49px;width:213px;height:39px;border:1px solid #cfd3d8;display:flex;align-items:center;gap:10px;padding-left:10px;font:700 14px "Open Sans",sans-serif;color:var(--ink);background:#fff}

/* nav */
.main-nav{height:41px;background:linear-gradient(#2a78c2,#0d4e95);display:flex;justify-content:center}
.main-nav ul{list-style:none;display:flex;height:100%}
.main-nav li{font:400 15px "Roboto Slab",Georgia,serif;color:var(--white);display:flex;align-items:center;padding:0 25px;border-left:1px solid rgba(255,255,255,.25)}
.main-nav li:last-child{border-right:1px solid rgba(255,255,255,.25)}

/* hero */
.hero{position:relative;height:504px}
.hero-visual{position:absolute;inset:0;background:linear-gradient(100deg,#3d4e62 0%,#6f8aa6 35%,#b9cde0 58%,#5f7894 80%,#2c3d52 100%)}
.hero-caption{position:absolute;left:0;right:0;bottom:0;height:58px;background:rgba(8,16,30,.75);display:flex;align-items:center;justify-content:center;font:400 27px "Raleway",sans-serif;color:var(--white)}
.hero-arrow{position:absolute;top:370px;width:32px;height:28px;background:rgba(20,20,20,.7);display:flex;align-items:center;justify-content:center}
.hero-arrow.prev{left:0}.hero-arrow.next{right:0}

/* section titles */
.section-title{text-align:center;font:400 28px "Roboto Slab",Georgia,serif;color:var(--navy);line-height:36px}
.section-title .accent{color:var(--blue)}
.title-rule{width:210px;height:1px;background:var(--line);margin:8px auto 0;position:relative}
.title-rule::after{content:"";position:absolute;left:50%;top:-1px;width:56px;height:3px;margin-left:-28px;background:var(--blue)}
.lead{font-size:11px;line-height:19px;text-align:center;color:var(--text)}

/* services */
.services{height:423px;padding-top:18px}
.services .lead{width:1120px;margin:20px auto 0}
.service-row{position:absolute;top:793px;left:162px;display:flex;gap:15px}
.service-hex{position:relative;width:208px;height:243px}
.service-hex svg{position:absolute;inset:0}
.service-label{position:absolute;left:0;right:0;top:168px;text-align:center;font:500 15px "Raleway",sans-serif;color:var(--white)}

/* welcome */
.welcome{height:294px;background:var(--grey-bg);padding-top:40px}
.welcome .title-rule{width:620px}
.welcome .lead{width:890px;margin:20px auto 0}
.read-more{display:flex;align-items:center;justify-content:center;width:123px;height:31px;margin:12px auto 0;background:var(--blue);color:var(--white);font:600 13px "Raleway",sans-serif}

/* why choose */
.why{position:relative;height:439px;background:linear-gradient(#1c6cb6,#163f7c 60%,#132d5e);overflow:hidden}
.why .section-title{color:var(--white);padding-top:46px}
.why .title-rule{width:150px;background:rgba(255,255,255,.3)}
.why-art{position:absolute;inset:0}
.feature{position:absolute;width:260px;color:var(--white)}
.feature h3{font:400 15px "Roboto Slab",Georgia,serif;line-height:18px}
.feature p{font-size:11px;line-height:17px;margin-top:4px;width:170px}
.feature.left{text-align:right}
.feature.left p{margin-left:90px}
.icon-disc{position:absolute;width:72px;height:72px;border-radius:50%;background:var(--white);display:flex;align-items:center;justify-content:center}
.core-name{position:absolute;left:500px;width:200px;top:362px;text-align:center;font:700 24px "Raleway",sans-serif;color:var(--blue-mid);letter-spacing:1px}

/* testimonials */
.testimonials{position:relative;height:314px;padding-top:70px}
.quote{width:780px;margin:30px auto 0;font:italic 14px/26px "Open Sans",sans-serif;text-align:center;color:var(--text)}
.quote-mark{position:absolute;font:700 54px Georgia,serif;color:#bbb}
.author{text-align:center;margin-top:14px;font:600 15px "Open Sans",sans-serif;color:var(--blue)}
.author-place{text-align:center;font-size:13px;color:var(--ink)}
.slide-arrow{position:absolute;top:170px}

/* clients */
.clients{height:211px;background:var(--grey-bg);padding-top:40px}
.client-row{display:flex;gap:32px;justify-content:center;margin-top:30px}
.client-tile{width:120px;height:69px;background:var(--white);border:1px solid #d7d7d7;display:flex;align-items:center;justify-content:center;gap:6px;font:600 15px "Raleway",sans-serif;color:#222}
.client-tile .dot{width:12px;height:12px;border-radius:50%;background:#222}

/* footer */
.site-footer{position:relative;height:282px;background:linear-gradient(#1e62aa,#173a72 60%,#132a57);color:var(--white)}
.foot-col{position:absolute;top:44px}
.foot-col h4{font:400 15px "Roboto Slab",Georgia,serif;padding-bottom:8px;border-bottom:1px solid rgba(255,255,255,.25);width:180px}
.quick-links{list-style:none;margin-top:10px}
.quick-links li{font-size:11px;line-height:22px}
.quick-links li::before{content:"› "}
.contact-line{display:flex;gap:10px;font-size:11px;line-height:15px;margin-top:12px;align-items:flex-start}
.c-icon{flex:none;width:18px;height:18px;border-radius:50%;background:var(--white)}
.field{width:208px;height:32px;background:var(--white);margin-top:8px;font-size:11px;color:#777;padding:8px}
.field.msg{height:56px}
.submit{width:80px;height:30px;background:var(--blue);margin-top:8px;font:500 15px "Raleway",sans-serif;display:flex;align-items:center;justify-content:center}
.foot-social{display:flex;gap:10px;margin-top:14px}
.foot-social span{width:30px;height:24px;border:1.5px solid rgba(255,255,255,.8);border-radius:50%}
.foot-brand{position:absolute;left:860px;top:150px;font:700 30px "Raleway",sans-serif;line-height:1;color:var(--white)}
.foot-brand small{display:block;font-size:11px;letter-spacing:2px;margin-top:4px}
.copyright{position:absolute;left:0;right:0;bottom:0;height:35px;background:#2b2b2b;color:#ddd;font-size:11px;display:flex;align-items:center;justify-content:center}
</style>
</head>
<body>

<header class="site-header">
  <div class="brand">
    <span class="brand-square"></span>
    <span class="brand-name"><span class="big">VELTRANE</span><span class="small">PROFESSIONAL SERVICES</span></span>
  </div>
  <div class="top-strip">
    <span class="top-phone"><span class="phone-dot"><svg width="12" height="12" viewBox="0 0 24 24"><path fill="#fff" d="M6.6 10.8a15 15 0 006.6 6.6l2.2-2.2a1 1 0 011-.3 11 11 0 003.6.6 1 1 0 011 1V20a1 1 0 01-1 1A17 17 0 013 4a1 1 0 011-1h3.5a1 1 0 011 1c0 1.3.2 2.5.6 3.6a1 1 0 01-.3 1z"/></svg></span>Call : 123-456-7890</span>
    <span class="social-ring"></span><span class="social-ring"></span><span class="social-ring"></span><span class="social-ring"></span>
  </div>
  <div class="schedule-btn">
    <svg width="26" height="26" viewBox="0 0 26 26"><rect x="2" y="4" width="22" height="20" fill="none" stroke="#142f5c" stroke-width="2"/><rect x="2" y="4" width="22" height="5" fill="#142f5c"/><path d="M9 13l3 3 5-5" fill="none" stroke="#1e6fb8" stroke-width="2"/></svg>
    Schedule Your Service
  </div>
</header>

<nav class="main-nav">
  <ul><li>Home</li><li>About Us</li><li>Presales &amp; Installation Services</li><li>Partners</li><li>Testimonials</li><li>Contact Us</li></ul>
</nav>

<section class="hero">
  <div class="hero-visual" role="img" aria-label="Business person touching a virtual interface of technology icons and a world map"></div>
  <div class="hero-arrow prev"><svg width="10" height="12"><path d="M8 1L2 6l6 5" fill="none" stroke="#fff" stroke-width="2"/></svg></div>
  <div class="hero-arrow next"><svg width="10" height="12"><path d="M2 1l6 5-6 5" fill="none" stroke="#fff" stroke-width="2"/></svg></div>
  <div class="hero-caption">We Provide Presales And Installation Services To IT/Telecom Company</div>
</section>

<section class="services">
  <h2 class="section-title">OUR <span class="accent">SERVICES</span></h2>
  <div class="title-rule"></div>
  <p class="lead">Lorem ipsum dolor sit amet, consectetuer adipiscing elit, sed diam nonummy nibh euismod tincidunt ut laoreet dolore magna aliquam erat volutpat. Ut wisi enim ad minim<br>veniam, quis nostrud exerci tation ullamcorper suscipit lobortis nisl ut aliquip ex ea</p>
  <div class="service-row">
    <div class="service-hex"><svg viewBox="0 0 208 243" role="img" aria-label="Office desk telephone photo"><defs><linearGradient id="g1" x1="0" y1="0" x2="0" y2="1"><stop offset="0" stop-color="#8a8f96"/><stop offset="1" stop-color="#2e3136"/></linearGradient></defs><path d="M104 4 L204 62 V181 L104 239 L4 181 V62Z" fill="url(#g1)" stroke="#1e6fb8" stroke-width="7"/></svg><div class="service-label">Managed VOIP Services</div></div>
    <div class="service-hex"><svg viewBox="0 0 208 243" role="img" aria-label="Green glowing fibre optic cables photo"><defs><linearGradient id="g2" x1="0" y1="0" x2="0" y2="1"><stop offset="0" stop-color="#6fd07a"/><stop offset="1" stop-color="#0d3d24"/></linearGradient></defs><path d="M104 4 L204 62 V181 L104 239 L4 181 V62Z" fill="url(#g2)" stroke="#1e6fb8" stroke-width="7"/></svg><div class="service-label">Fibre Service</div></div>
    <div class="service-hex"><svg viewBox="0 0 208 243" role="img" aria-label="Businessman with network communication graphics photo"><defs><linearGradient id="g3" x1="0" y1="0" x2="0" y2="1"><stop offset="0" stop-color="#7d8590"/><stop offset="1" stop-color="#1d2229"/></linearGradient></defs><path d="M104 4 L204 62 V181 L104 239 L4 181 V62Z" fill="url(#g3)" stroke="#1e6fb8" stroke-width="7"/></svg><div class="service-label">Managed Comms</div></div>
    <div class="service-hex"><svg viewBox="0 0 208 243" role="img" aria-label="Call centre agent with headset photo"><defs><linearGradient id="g4" x1="0" y1="0" x2="0" y2="1"><stop offset="0" stop-color="#c9b9a6"/><stop offset="1" stop-color="#3b2e26"/></linearGradient></defs><path d="M104 4 L204 62 V181 L104 239 L4 181 V62Z" fill="url(#g4)" stroke="#1e6fb8" stroke-width="7"/></svg><div class="service-label">Inbound Voice</div></div>
  </div>
</section>

<section class="welcome">
  <h2 class="section-title">WELCOME TO VELTRANE <span class="accent">PROFESSIONAL SERVICES</span></h2>
  <div class="title-rule"></div>
  <p class="lead">Lorem ipsum dolor sit amet, consectetuer adipiscing elit, sed diam nonummy nibh euismod tincidunt ut laoreet dolore magna aliquam erat volutpat. Ut wisi enim ad minim veniam, quis nostrud exerci tation ullamcorper suscipit lobortis nisl ut aliquip ex ea commodo consequat. Duis autem vel eum iriure dolor in hendrerit in vulputate velit esse molestie consequat, vel illum dolore eu feugiat nulla facilisis at vero eros et accu nonummy nibh euismod tincidunt ut laoreet dolore magna aliquam erat volutpat. Ut wisi enim ad minim veniam, quis nostrud exerci tation ullamcorper suscipit lobortis nisl ut aliquip ex ea commodo consequat. Duis autmsan et iusto odio dignissim qui blandit praesent luptatum zzril delenit augue duis dolore te feugait nulla facilisi.</p>
  <div class="read-more">Read More</div>
</section>

<section class="why">
  <h2 class="section-title">Why Choose Us</h2>
  <div class="title-rule"></div>
  <svg class="why-art" width="1200" height="439" viewBox="0 0 1200 439">
    <path d="M437 439 A163 163 0 0 1 763 439Z" fill="#fff" stroke="#1e6fb8" stroke-width="5"/>
    <g stroke="#fff" stroke-width="1.5" stroke-dasharray="3 4" fill="none">
      <line x1="414" y1="392" x2="446" y2="398"/>
      <line x1="465" y1="295" x2="485" y2="325"/>
      <line x1="540" y1="245" x2="558" y2="287"/>
      <line x1="660" y1="245" x2="642" y2="287"/>
      <line x1="735" y1="295" x2="715" y2="325"/>
      <line x1="786" y1="392" x2="754" y2="398"/>
    </g>
    <g fill="#fff" stroke="#1e6fb8" stroke-width="3">
      <circle cx="446" cy="398" r="6"/><circle cx="485" cy="325" r="6"/><circle cx="558" cy="287" r="6"/>
      <circle cx="642" cy="287" r="6"/><circle cx="715" cy="325" r="6"/><circle cx="754" cy="398" r="6"/>
    </g>
  </svg>
  <div class="core-name">VELTRANE</div>

  <div class="icon-disc" style="left:343px;top:329px"><svg width="36" height="36" viewBox="0 0 24 24"><circle cx="12" cy="10" r="6" fill="#142f5c"/><rect x="9" y="16" width="6" height="4" fill="#142f5c"/></svg></div>
  <div class="icon-disc" style="left:394px;top:232px"><svg width="36" height="36" viewBox="0 0 24 24"><circle cx="12" cy="12" r="6" fill="none" stroke="#142f5c" stroke-width="4" stroke-dasharray="3 2"/><circle cx="12" cy="12" r="3" fill="#142f5c"/></svg></div>
  <div class="icon-disc" style="left:500px;top:175px"><svg width="34" height="34" viewBox="0 0 24 24"><path fill="#142f5c" d="M6.6 10.8a15 15 0 006.6 6.6l2.2-2.2a1 1 0 011-.3 11 11 0 003.6.6 1 1 0 011 1V20a1 1 0 01-1 1A17 17 0 013 4a1 1 0 011-1h3.5a1 1 0 011 1c0 1.3.2 2.5.6 3.6a1 1 0 01-.3 1z"/></svg></div>
  <div class="icon-disc" style="left:626px;top:175px"><svg width="34" height="34" viewBox="0 0 24 24"><circle cx="10" cy="8" r="4" fill="#142f5c"/><path d="M3 21a7 7 0 0114 0z" fill="#142f5c"/><circle cx="18" cy="6" r="3.5" fill="none" stroke="#142f5c" stroke-width="1.5"/></svg></div>
  <div class="icon-disc" style="left:732px;top:232px"><svg width="34" height="34" viewBox="0 0 24 24"><rect x="2" y="4" width="16" height="15" fill="none" stroke="#142f5c" stroke-width="2"/><rect x="2" y="4" width="16" height="4" fill="#142f5c"/><circle cx="18" cy="17" r="5" fill="#fff" stroke="#142f5c" stroke-width="2"/></svg></div>
  <div class="icon-disc" style="left:785px;top:326px"><svg width="36" height="36" viewBox="0 0 24 24"><circle cx="9" cy="8" r="3.5" fill="#142f5c"/><circle cx="16" cy="9" r="3" fill="#142f5c"/><path d="M2 20a7 7 0 0114 0zM13 20a5 5 0 019 0z" fill="#142f5c"/></svg></div>

  <div class="feature left" style="left:242px;top:137px"><h3>Unbiased Recommendations</h3><p>Lorem ipsum dolor sit mork adipiscing sed diam</p></div>
  <div class="feature right" style="left:721px;top:137px"><h3>Expert Guidance</h3><p>Lorem ipsum dolor sit mork adipiscing sed diam</p></div>
  <div class="feature left" style="left:115px;top:220px"><h3>Unparalleled<br>Service</h3><p>Lorem ipsum dolor sit mork dipiscing sed diam</p></div>
  <div class="feature right" style="left:826px;top:232px"><h3>Considerable Time<br>For You</h3><p>Lorem ipsum dolor sit mork adipiscing sed diam</p></div>
  <div class="feature left" style="left:62px;top:331px"><h3>Superior Advice</h3><p>Lorem ipsum dolor sit mork adipiscing sed diam</p></div>
  <div class="feature right" style="left:879px;top:331px"><h3>Deep Legal Industry<br>Relationships</h3><p>Lorem ipsum dolor sit mork adipiscing sed diam</p></div>
</section>

<section class="testimonials">
  <h2 class="section-title">Clients <span class="accent">Testimonials</span></h2>
  <div class="title-rule"></div>
  <span class="quote-mark" style="left:192px;top:130px">“</span>
  <p class="quote">Lorem ipsum dolor sit amet, consectetuer adipiscing elit, sed diam nonummy nibh euismod tinciduntol ut laoreet dolore magna aliquam erat volutpat. Ut wisi enim ad minim veniam, quis nostrud exercimori mornkle tation ullamcorper suscipit lobortis nisl ut aliquip ex ea commodo consequat.</p>
  <span class="quote-mark" style="left:770px;top:208px">”</span>
  <div class="author">Marla T.</div>
  <div class="author-place">Costa Mesa, CA</div>
  <svg class="slide-arrow" style="left:132px" width="26" height="48"><path d="M24 2L3 24l21 22" fill="none" stroke="#aaa" stroke-width="1.5"/></svg>
  <svg class="slide-arrow" style="left:1040px" width="26" height="48"><path d="M2 2l21 22L2 46" fill="none" stroke="#aaa" stroke-width="1.5"/></svg>
</section>

<section class="clients">
  <h2 class="section-title">OUR <span class="accent">CLIENTS</span></h2>
  <div class="title-rule"></div>
  <div class="client-row">
    <div class="client-tile"><span class="dot"></span>Norvane</div>
    <div class="client-tile">Kellbrook</div>
    <div class="client-tile">Quintra</div>
    <div class="client-tile">Ostrel Systems</div>
    <div class="client-tile">Lumadex</div>
    <div class="client-tile"><span class="dot"></span>Norvane</div>
  </div>
</section>

<footer class="site-footer">
  <div class="foot-col" style="left:164px">
    <h4>Quick Links</h4>
    <ul class="quick-links"><li>Home</li><li>About Us</li><li>Presales &amp; Installation Service</li><li>Testimonials</li><li>Our Clients</li><li>Contact Us</li></ul>
  </div>
  <div class="foot-col" style="left:366px">
    <h4>Contact Details</h4>
    <div class="contact-line"><span class="c-icon"></span><span>Veltrane Professional Services<br><b>Street Name City Name<br>State Zipcode</b></span></div>
    <div class="contact-line"><span class="c-icon"></span><span>123-456-7890</span></div>
    <div class="contact-line"><span class="c-icon"></span><span>123-456-7890</span></div>
    <div class="contact-line"><span class="c-icon"></span><span>inquiry@veltraneprofessional.example</span></div>
  </div>
  <div class="foot-col" style="left:618px">
    <h4>Quick Inquiry</h4>
    <div class="field">Name</div>
    <div class="field">Email</div>
    <div class="field msg">Message</div>
    <div class="submit">Submit</div>
  </div>
  <div class="foot-col" style="left:860px">
    <h4 style="width:160px">Follow Us</h4>
    <div class="foot-social"><span></span><span></span><span></span><span></span></div>
  </div>
  <div class="foot-brand">VELTRANE<small>PROFESSIONAL SERVICES</small></div>
  <div class="copyright">Copyright © 2017 Veltrane Professional Services . All Rights Reserved.</div>
</footer>

</body>
</html>
```